Electrical panel service sticker w Bucket truck & Logo

We have a rather plain sticker we put on lighting panels to remind customers who to call for service. We want to redesign them with brushed aluminum background. We want a remake of the sticker with the outline of a bucket truck. You'll need to find or draw the outling of a bucket truck maybe with the boom up slightly as we will get these stickers die cut.

We want LOGO with Ph.# and Email.
Electrical * Lighting * Sign Service

Target Market(s)

Commercial property managers

Industry/Entity Type

Property Management

Requirements
Must have
• Bucket Truck Outline

```html
<!DOCTYPE html>
<html lang="en">
<head>
<meta charset="utf-8">
<title>Brightline Fixtures – Panel Service Sticker</title>
<link rel="stylesheet" href="https://fonts.googleapis.com/css2?family=Montserrat:wght@600;700&family=Open+Sans:wght@400&family=Oswald:wght@500;700&display=swap">
<style>
  :root {
    --backdrop: #3f3f3f;
    --alu-light: #f2f2f2;
    --alu-mid: #c9cacc;
    --alu-dark: #a9abae;
    --brand-red: #e8151f;
    --brand-blue: #1f3185;
    --ink: #0d0d0d;
    --truck-tone: #151515;
  }
  * { margin: 0; padding: 0; box-sizing: border-box; }
  html, body { width: 1200px; height: 1200px; overflow: hidden; background: var(--backdrop); }
  .canvas { position: relative; width: 1200px; height: 1200px; }
  .sticker-shape { position: absolute; inset: 0; }
  .truck-art {
    position: absolute; left: 167px; top: 347px; width: 342px; height: 304px;
    background: var(--truck-tone); border-radius: 10px;
  }
  .brand-name {
    position: absolute; left: 520px; top: 388px; width: 505px;
    font-family: 'Oswald', sans-serif; font-weight: 700; color: var(--brand-red);
    text-align: center; text-transform: uppercase; line-height: 1;
  }
  .brand-name .line-1 { display: block; font-size: 92px; letter-spacing: 2px; }
  .brand-name .line-2 { display: block; font-size: 92px; letter-spacing: 3px; margin-top: 6px; }
  .brand-suffix {
    position: absolute; left: 600px; width: 290px; top: 572px; text-align: center;
    font-family: 'Open Sans', sans-serif; font-size: 30px; color: var(--brand-blue); letter-spacing: .5px;
  }
  .phone {
    position: absolute; left: 600px; width: 290px; top: 606px; text-align: center;
    font-family: 'Oswald', sans-serif; font-weight: 700; font-size: 56px; line-height: 1.05;
    color: var(--brand-red); transform: scaleX(.86);
  }
  .email {
    position: absolute; left: 190px; top: 668px; display: flex; align-items: center; gap: 10px;
    font-family: 'Montserrat', sans-serif; font-weight: 600; font-size: 39px; color: var(--brand-blue);
  }
  .email svg { width: 36px; height: 36px; }
  .services {
    position: absolute; left: 120px; width: 962px; top: 720px; display: flex; justify-content: center; align-items: center; gap: 14px;
    font-family: 'Oswald', sans-serif; font-weight: 500; font-size: 60px; color: var(--ink);
  }
  .services .star { width: 28px; height: 28px; }
  .website {
    position: absolute; left: 120px; width: 962px; top: 788px; text-align: center;
    font-family: 'Montserrat', sans-serif; font-weight: 700; font-size: 38px; color: var(--brand-blue);
  }
</style>
</head>
<body>
<main class="canvas">
  <svg class="sticker-shape" viewBox="0 0 1200 1200" aria-hidden="true">
    <defs>
      <linearGradient id="brushed-aluminum" x1="0" y1="0" x2="1" y2="1">
        <stop offset="0" stop-color="var(--alu-mid)"/>
        <stop offset=".3" stop-color="var(--alu-light)"/>
        <stop offset=".55" stop-color="var(--alu-mid)"/>
        <stop offset=".8" stop-color="var(--alu-light)"/>
        <stop offset="1" stop-color="var(--alu-dark)"/>
      </linearGradient>
    </defs>
    <path class="die-cut" fill="url(#brushed-aluminum)"
      d="M115 375 H197 V345 L253 336 L288 345 L328 375 H1088 V859 H115 Z"/>
    <path class="red-frame" fill="none" stroke="var(--brand-red)" stroke-width="2.5"
      d="M200 387 H129 V842 H1069 V387 H347"/>
  </svg>

  <div class="truck-art" role="img" aria-label="Black silhouette illustration of a bucket truck with its boom raised"></div>

  <h1 class="brand-name">
    <span class="line-1">Brightline</span>
    <span class="line-2">Fixtures</span>
  </h1>
  <p class="brand-suffix">INCORPORATED</p>
  <p class="phone">877.555.0148</p>

  <p class="email">
    <svg viewBox="0 0 36 36" aria-hidden="true">
      <rect x="9" y="2" width="18" height="18" fill="#fff" stroke="var(--brand-red)" stroke-width="2"/>
      <path d="M12 8h12M12 12h12M12 16h8" stroke="var(--brand-red)" stroke-width="2"/>
      <path d="M2 14 L18 26 L34 14 V34 H2 Z" fill="var(--brand-red)"/>
      <path d="M2 34 L15 23 M34 34 L21 23" stroke="#fff" stroke-width="1.5"/>
    </svg>
    Service@BrightlineFixtures.com
  </p>

  <p class="services">
    <span>ELECTRICAL</span>
    <svg class="star" viewBox="0 0 24 24" aria-hidden="true"><path fill="var(--brand-red)" d="M12 1l3.2 7.2 7.8.7-5.9 5.2 1.8 7.7L12 17.8 5.1 21.8l1.8-7.7L1 8.9l7.8-.7z"/></svg>
    <span>LIGHTING</span>
    <svg class="star" viewBox="0 0 24 24" aria-hidden="true"><path fill="var(--brand-red)" d="M12 1l3.2 7.2 7.8.7-5.9 5.2 1.8 7.7L12 17.8 5.1 21.8l1.8-7.7L1 8.9l7.8-.7z"/></svg>
    <span>SIGN SERVICE</span>
  </p>

  <p class="website">www.BrightlineFixtures.com</p>
</main>
</body>
</html>
```